Korean Homemade food restaurant just like what your mom cooks at home

I need a black and white simple and modern design according to my logo.
My restaurant name is Noru Kan (meaning of home cooking).
I need to have 솔찬(Noru Kan) in Korean need to be included. Once again 솔찬.
I am not sure if I need to include my name and number and adress.

솔찬 Noru Kan 418 Marlow Ct. Clarksville, TN 37512 Grant Oh Owner Cell:931-555-0183 Store:931-555-0297

Target Market(s)

business owners, university students

Industry/Entity Type

Restaurant

Contact Information for Business Card

This is traditional Korean food restaurant that targets university students during lunch and Korean business travelers at dinner.

Font styles to use
Sans Serif

Requirements
Must have
• Must have my logo.

```html
<!DOCTYPE html>
<html lang="en">
<head>
<meta charset="utf-8">
<title>Noru Kan — Business Card</title>
<link rel="stylesheet" href="https://fonts.googleapis.com/css2?family=Exo+2:wght@300;400;500&family=Noto+Sans+KR:wght@300;400&display=swap">
<style>
  :root {
    --page-bg: #c9ccd2;
    --page-bg-light: #e4e6ea;
    --card-grey: #dcdcdc;
    --ink: #151515;
    --ink-soft: #3a3a3a;
    --on-dark: #f2f2f2;
    --stripe: #b9b9b9;
  }
  * { margin: 0; padding: 0; box-sizing: border-box; }
  html, body { width: 1200px; height: 866px; overflow: hidden; }
  body {
    background: radial-gradient(ellipse at 75% 80%, var(--page-bg-light), var(--page-bg) 70%);
    font-family: "Exo 2", "Noto Sans KR", sans-serif;
    color: var(--ink);
    position: relative;
  }
  .card {
    position: absolute;
    width: 540px; height: 310px;
    background: radial-gradient(ellipse at 50% 50%, #ffffff, var(--card-grey) 120%);
    box-shadow: 0 10px 24px rgba(0,0,0,0.18);
    overflow: hidden;
  }
  .card--front { left: 40px; top: 130px; }
  .card--back { left: 620px; top: 420px; }

  .wordmark { display: flex; align-items: center; gap: 12px; }
  .wordmark__dot { width: 34px; height: 34px; border-radius: 50%; background: var(--ink); flex: none; }
  .wordmark__text { display: flex; flex-direction: column; align-items: flex-start; }
  .wordmark__name {
    font-family: "Exo 2", sans-serif;
    font-weight: 400; color: var(--ink); letter-spacing: 0.5px; line-height: 1.05;
  }
  .wordmark__korean {
    font-family: "Noto Sans KR", sans-serif;
    font-weight: 400; color: var(--ink); letter-spacing: 2px; line-height: 1.2;
  }
  .card--front .wordmark {
    position: absolute; left: 50%; top: 50%;
    transform: translate(-50%, -50%);
  }
  .card--front .wordmark__dot { width: 46px; height: 46px; }
  .card--front .wordmark__name { font-size: 46px; }
  .card--front .wordmark__korean { font-size: 20px; margin-top: 4px; }

  .back-shape { position: absolute; inset: 0; }
  .card--back .wordmark { position: absolute; left: 34px; top: 52px; }
  .card--back .wordmark__name { font-size: 32px; }
  .card--back .wordmark__korean { font-size: 14px; margin-top: 2px; }

  .person { position: absolute; right: 30px; top: 34px; text-align: right; }
  .person__name { font-weight: 500; font-size: 15px; letter-spacing: 1.5px; text-transform: uppercase; }
  .person__role { font-weight: 300; font-size: 11.5px; color: var(--ink-soft); letter-spacing: 0.5px; }

  .location {
    position: absolute; right: 30px; top: 138px; text-align: right;
    color: var(--on-dark); font-size: 11px; font-weight: 300; line-height: 1.5; letter-spacing: 0.5px;
  }
  .website {
    position: absolute; right: 30px; top: 200px;
    color: var(--on-dark); font-size: 11px; font-weight: 300; letter-spacing: 0.6px;
  }

  .contacts {
    position: absolute; left: 26px; top: 226px; list-style: none;
    color: var(--on-dark); font-size: 10.5px; font-weight: 300; letter-spacing: 0.5px;
  }
  .contacts li { display: flex; align-items: center; gap: 8px; height: 18px; }
  .contacts svg { width: 11px; height: 11px; fill: var(--on-dark); }
</style>
</head>
<body>

  <section class="card card--front" aria-label="Card front">
    <div class="wordmark">
      <span class="wordmark__dot"></span>
      <span class="wordmark__text">
        <span class="wordmark__name">Noru Kan</span>
        <span class="wordmark__korean" lang="ko">솔찬</span>
      </span>
    </div>
  </section>

  <section class="card card--back" aria-label="Card back">
    <svg class="back-shape" viewBox="0 0 540 310" preserveAspectRatio="none" aria-hidden="true">
      <path d="M0,200 C170,196 350,140 540,82 L540,92 C350,150 170,206 0,212 Z" fill="var(--stripe)"/>
      <path d="M0,214 C170,208 350,154 540,96 L540,310 L0,310 Z" fill="var(--ink)"/>
    </svg>

    <div class="wordmark">
      <span class="wordmark__dot"></span>
      <span class="wordmark__text">
        <span class="wordmark__name">Noru Kan</span>
        <span class="wordmark__korean" lang="ko">솔찬</span>
      </span>
    </div>

    <div class="person">
      <p class="person__name">Grant Oh</p>
      <p class="person__role">Owner</p>
    </div>

    <p class="location">418 Marlow Ct.<br>Clarksville, TN 37512</p>
    <p class="website">www.norukan.example</p>

    <ul class="contacts">
      <li>
        <svg viewBox="0 0 24 24"><path d="M6.6 10.8a15.1 15.1 0 0 0 6.6 6.6l2.2-2.2a1 1 0 0 1 1-.25 11.4 11.4 0 0 0 3.6.57 1 1 0 0 1 1 1V20a1 1 0 0 1-1 1A17 17 0 0 1 3 4a1 1 0 0 1 1-1h3.5a1 1 0 0 1 1 1c0 1.25.2 2.45.57 3.57a1 1 0 0 1-.25 1z"/></svg>
        931-555-0297
      </li>
      <li>
        <svg viewBox="0 0 24 24"><path d="M7 1h10a2 2 0 0 1 2 2v18a2 2 0 0 1-2 2H7a2 2 0 0 1-2-2V3a2 2 0 0 1 2-2zm0 3v14h10V4zm5 15.5a1 1 0 1 0 0 2 1 1 0 0 0 0-2z"/></svg>
        931-555-0183
      </li>
      <li>
        <svg viewBox="0 0 24 24"><path d="M6 2h9l3 3v5H6zM4 11h16a2 2 0 0 1 2 2v8H2v-8a2 2 0 0 1 2-2zm3 3v2h4v-2zm0 4v1h10v-1z"/></svg>
        931-555-0346
      </li>
      <li>
        <svg viewBox="0 0 24 24"><path d="M2 5h20v14H2zm2 2v.5l8 5.5 8-5.5V7zm0 3v7h16v-7l-8 5.5z"/></svg>
        hello@norukan.example
      </li>
    </ul>
  </section>

</body>
</html>
```